flyer design for landscape group. i have enclosed my business card with logo

we are a local domestic and commercial landscaping group based in wokingham berkshire .we offer competitive landscaping solutions with a broad knowledge helping us solve problems in many fields such as new lawns, lawn care,tree care ,tree removal,hard and soft landscaping, decking, fencing ,garden or land clearance or just helping you with general maintanence. Being fully insured and certified for the job ,our excellent attention to detail has seen us recognised by local authorities and work for them on maintenance programmes performing in a safe and efficient manner

Target Market(s)

high end gardens commercial property

Industry/Entity Type

Landscaping

Requirements
Must have
• my logo . and some minimal sleek black and white design with small injections of colour
Should not have
• please do not include my full name or address only email and telephone

```html
<!DOCTYPE html>
<html lang="en">
<head>
<meta charset="utf-8">
<title>Grovewell Berkshire – Flyer Front &amp; Back</title>
<link rel="stylesheet" href="https://fonts.googleapis.com/css2?family=Great+Vibes&family=Questrial&family=Quicksand:wght@500&display=swap">
<style>
  :root {
    --orange: #f7860f;
    --ink: #3a2a22;
    --band: rgba(38, 38, 38, 0.78);
    --paper: #ebebeb;
    --ring: #5a5a5a;
    --divider: #4f6b55;
    --bg-light: #f4f4f4;
    --bg-dark: #c9c9c9;
  }
  * { margin: 0; padding: 0; box-sizing: border-box; }
  html, body { width: 1200px; height: 1000px; overflow: hidden; }
  body {
    position: relative;
    background: radial-gradient(ellipse at 45% 45%, var(--bg-light) 0%, var(--bg-dark) 100%);
    font-family: "Questrial", sans-serif;
  }
  .flyer-side {
    position: absolute;
    left: 100px;
    width: 660px;
    height: 466px;
    overflow: hidden;
    box-shadow: 4px 6px 10px rgba(0,0,0,0.35);
  }
  .flyer-front { top: 22px; }
  .flyer-back { top: 507px; }

  .foliage-photo {
    position: absolute; inset: 0;
    background:
      radial-gradient(circle at 20% 30%, #3d3d3d 0%, transparent 45%),
      radial-gradient(circle at 80% 70%, #444 0%, transparent 40%),
      linear-gradient(135deg, #9a9a9a 0%, #5c5c5c 50%, #8a8a8a 100%);
  }
  .front-band {
    position: absolute; left: 0; right: 0; top: 83px; height: 300px;
    background: var(--band);
  }
  .brand-disc {
    position: absolute; left: 205px; top: 105px;
    width: 250px; height: 250px; border-radius: 50%;
    border: 6px solid var(--ring);
    background: var(--paper);
    display: flex; flex-direction: column; align-items: center; justify-content: center;
  }
  .brand-name {
    font-family: "Questrial", sans-serif;
    color: var(--ink);
    font-size: 38px;
    letter-spacing: 1px;
    line-height: 1.1;
    text-align: center;
  }
  .brand-name .region { display: block; font-size: 14px; letter-spacing: 3px; }
  .front-contact {
    position: absolute; left: 0; right: 0; top: 343px;
    text-align: center; color: var(--orange);
    font-size: 13px; letter-spacing: 1.5px; line-height: 16px;
  }
  .front-contact .phone { font-size: 14px; letter-spacing: 2.5px; }

  .house-photo {
    position: absolute; inset: 0;
    background:
      linear-gradient(180deg, #b4b4b4 0%, #7a7a7a 35%, #4a4a4a 70%, #3a3a3a 100%);
  }
  .back-band { position: absolute; inset: 0; }
  .back-title {
    position: absolute; left: 0; right: 0; top: 158px;
    text-align: center;
    font-family: "Great Vibes", cursive;
    color: var(--orange);
    font-size: 50px;
  }
  .service-list {
    position: absolute; left: 0; right: 0; top: 232px;
    text-align: center; color: #fff;
    font-family: "Quicksand", sans-serif; font-weight: 500;
    font-size: 16.5px; line-height: 19.5px;
    list-style: none;
  }
  .service-list .sep { color: var(--divider); margin: 0 3px; }

  .side-label {
    position: absolute; left: 945px; top: 350px; width: 170px;
    text-align: center; color: var(--orange);
    font-family: "Questrial", sans-serif;
    font-size: 72px; line-height: 82px;
  }
  .label-bracket { position: absolute; left: 0; top: 0; }
</style>
</head>
<body>

<section class="flyer-side flyer-front">
  <div class="foliage-photo" role="img" aria-label="Black and white photograph of dense leaves and foliage"></div>
  <div class="front-band"></div>
  <div class="brand-disc">
    <p class="brand-name">GROVEWELL<span class="region">BERKSHIRE</span></p>
  </div>
  <p class="front-contact">
    <span class="phone">0770 412 3398</span><br>
    www.grovewellberkshire.co.uk
  </p>
</section>

<section class="flyer-side flyer-back">
  <div class="house-photo" role="img" aria-label="Black and white photograph of a large house with a lawn and trees"></div>
  <svg class="back-band" width="660" height="466" viewBox="0 0 660 466">
    <polygon points="0,180 545,0 660,0 660,300 125,466 0,466" fill="rgba(20,20,20,0.9)"/>
  </svg>
  <h2 class="back-title">Landscaping Solutions</h2>
  <ul class="service-list">
    <li>New lawn<span class="sep">|</span>Lawn care<span class="sep">|</span>Tree care<span class="sep">|</span>Tree removal</li>
    <li>Hard and soft landscaping<span class="sep">|</span>Decking</li>
    <li>Fencing<span class="sep">|</span>Garden or land clearance</li>
    <li>General maintanence</li>
  </ul>
</section>

<svg class="label-bracket" width="1200" height="1000" viewBox="0 0 1200 1000" fill="none" stroke="#f7860f" stroke-width="4">
  <polyline points="778,231 825,231 825,768 778,768"/>
  <line x1="825" y1="499" x2="895" y2="499"/>
  <polyline points="935,383 895,383 895,563 935,563"/>
</svg>
<p class="side-label">front<br>&amp;<br>Back</p>

</body>
</html>
```